BLUE FORGE (Business Card for Training Company)

Blue Forge is a training and consultancy company with a focus on executive protection and medical. I would like the card to be nice and sharp, not overdone and in black and red. I would also like it to highlight that it is "A Tavmont Company"

I would like it to be simple and highlight a few things.

1. Name
2. Title
3. Phone Number
4. Email

I would also like www.tavmontgroup.example/blue-forge to be on the card somewhere.

Target Market(s)

Security Companies

Industry/Entity Type

Security

Contact Information for Business Card

Blue Forge is a training and consultancy company with a focus on executive protection and medical. I would like the card to be nice and sharp, not overdone and in black and red. I would also like it to highlight that it is "A Tavmont Company" I would like it to be simple and highlight a few things. 1. Name 2. Title 3. Phone Number 4. Email I would also like www.tavmontgroup.example/blue-forge to be on the card somewhere.

Requirements
Must have
• A Tavmont Company listed on the card and the website
Nice to have
• Highlight Medical Training, Consultancy & Executive Protection Courses

```html
<!DOCTYPE html>
<html lang="en">
<head>
<meta charset="utf-8">
<title>Blue Forge — Business Card</title>
<link rel="stylesheet" href="https://fonts.googleapis.com/css2?family=Roboto:wght@500;700&family=Roboto+Condensed:wght@400;700&display=swap">
<style>
  :root {
    --backdrop: #dcdcdc;
    --card: #f7f7f7;
    --brand-red: #6b0000;
    --ink: #1a1a1a;
    --muted: #4a4a4a;
    --white: #ffffff;
  }
  * { margin: 0; padding: 0; box-sizing: border-box; }
  html, body {
    width: 1200px; height: 1200px; overflow: hidden;
    background: var(--backdrop);
  }
  .canvas { position: relative; width: 1200px; height: 1200px; }
  .card {
    position: absolute; left: 262px; width: 686px; height: 392px;
    background: var(--card); overflow: hidden;
  }
  .card--front { top: 165px; }
  .card--back { top: 653px; }

  .wordmark {
    font-family: "Roboto Condensed", sans-serif;
    font-weight: 700; color: var(--brand-red);
    text-transform: uppercase; line-height: 0.9; letter-spacing: 1px;
  }
  .card--front .wordmark { position: absolute; left: 74px; top: 78px; font-size: 48px; }
  .card--back .wordmark { position: absolute; left: 188px; top: 108px; font-size: 82px; }

  .parent-line {
    position: absolute; left: 74px; top: 174px;
    font-family: "Roboto", sans-serif; font-weight: 500;
    font-size: 15px; letter-spacing: 3.2px; color: var(--muted);
    text-transform: uppercase;
  }

  .contact-list {
    position: absolute; left: 74px; top: 266px; list-style: none;
    font-family: "Roboto Condensed", sans-serif; font-size: 17px; color: var(--muted);
  }
  .contact-list li { display: flex; align-items: center; height: 22px; }
  .contact-list svg { width: 14px; height: 14px; margin-right: 9px; fill: var(--brand-red); }

  .person {
    position: absolute; right: 55px; top: 278px; text-align: right;
  }
  .person__name {
    font-family: "Roboto", sans-serif; font-weight: 700; font-size: 24px;
    color: var(--brand-red); text-transform: uppercase; letter-spacing: -0.3px;
  }
  .person__title {
    font-family: "Roboto Condensed", sans-serif; font-size: 17px; color: var(--ink);
  }
  .accent-bar {
    position: absolute; left: 678px; top: 279px; width: 8px; height: 41px;
    background: var(--brand-red);
  }

  .tagline-band {
    position: absolute; left: 0; top: 334px; width: 100%; height: 31px;
    background: var(--brand-red); color: var(--white);
    font-family: "Roboto Condensed", sans-serif; font-size: 17px; letter-spacing: 1.6px;
    line-height: 31px; padding-left: 73px;
  }
</style>
</head>
<body>
<main class="canvas">
  <section class="card card--front">
    <div class="wordmark">Blue<br>Forge</div>
    <p class="parent-line">A Tavmont Company</p>
    <ul class="contact-list">
      <li><svg viewBox="0 0 24 24" aria-hidden="true"><path d="M6.6 10.8a15.1 15.1 0 0 0 6.6 6.6l2.2-2.2a1 1 0 0 1 1-.25 11.4 11.4 0 0 0 3.6.57 1 1 0 0 1 1 1V20a1 1 0 0 1-1 1A17 17 0 0 1 3 4a1 1 0 0 1 1-1h3.5a1 1 0 0 1 1 1c0 1.25.2 2.45.57 3.57a1 1 0 0 1-.25 1z"/></svg>555-014-2730</li>
      <li><svg viewBox="0 0 24 24" aria-hidden="true"><path d="M2 5h20v14H2z M2 5l10 7 10-7" /></svg>info@tavmontgroup.example</li>
      <li><svg viewBox="0 0 24 24" aria-hidden="true"><path d="M12 2a10 10 0 1 0 0 20 10 10 0 0 0 0-20zm-1 17.9A8 8 0 0 1 4.1 9.9L9 15v1a2 2 0 0 0 2 2zm6.9-2.5A2 2 0 0 0 16 16h-1v-3a1 1 0 0 0-1-1H8v-2h2a1 1 0 0 0 1-1V7h2a2 2 0 0 0 2-2v-.4a8 8 0 0 1 2.9 12.8z"/></svg>tavmontgroup.example</li>
    </ul>
    <div class="person">
      <p class="person__name">Daniel Harper</p>
      <p class="person__title">President</p>
    </div>
    <div class="accent-bar"></div>
  </section>

  <section class="card card--back">
    <div class="wordmark">Blue<br>Forge</div>
    <p class="tagline-band">Medical Training, Consultancy &amp; Executive Protection Courses</p>
  </section>
</main>
</body>
</html>
```